Brightway Inc. Business Card Design

Brightway Inc. is in search of a great clean design for our business cards!

Looking to incorporate our full logo and watermark on side one (however, I am open to having the text and watermark separated within the design.)

On side two, I am looking to have contact information (Name, Position, Phone #, Email, Website (www.thebrightway.ca). Can have the logo and/or watermark as part of the design if applicable.

Please add tagline "Where Shine Counts" on either side 1 or 2. This tagline can be in a sans serif, serif or cursive font as long as it compliments overall design. Capitalization can be title or sentence case depending on how it fits within the design.

Get creative!! Looking for a clean, crisp, premium design! Looking for a glossy card finish with spot UV features when printed. Cards will also be printed with rounded corners. Standard dimensions (3.5 x 2).

Target Market(s)

B2B - primary clients are business owners or property management corporations. (residential jobs are few and far between)

Industry/Entity Type

Business

Contact Information for Business Card

- clean, crisp design
- double sided
- spot UV accents and glossy finish upon printing
- standard business card size (3.5 x 2) with rounded corners
- please see project description for requirements per side

Font styles to use
Sans Serif

Requirements
Must have
• - adequate bleeds with print ready files
• - cohesive design elements between side 1 & 2
• - spot UV elements (can be on both sides or just one, use your discretion)
• - colour pallet should match the logo file provided
• - incorporate tagline "where shine counts" (this tagline can be in a serif or sans serif font as long as it is complimentary to the overall design.
Nice to have
• - Premium elements with a clean design
Should not have
• - Please omit cartoon or whimsical like designs, think premium.
• - Colours should not stray from the pallet of the provided logo.

```html
<!DOCTYPE html>
<html lang="en">
<head>
<meta charset="utf-8">
<title>Brightway Inc. Business Card</title>
<link href="https://fonts.googleapis.com/css2?family=Work+Sans:wght@400;500;700&display=swap" rel="stylesheet">
<style>
  :root {
    --navy: #1d2663;
    --navy-deep: #151c4d;
    --teal: #22b8b8;
    --teal-light: #5fd3d0;
    --white: #ffffff;
    --backdrop: #2b2b2b;
    --rule-light: rgba(255,255,255,0.55);
    --rule-dark: #3a4170;
  }
  * { box-sizing: border-box; margin: 0; padding: 0; }
  html, body {
    width: 1200px; height: 930px; overflow: hidden;
    background: var(--backdrop);
    font-family: "Work Sans", sans-serif;
  }
  .sheet {
    position: relative; width: 1200px; height: 930px;
    display: flex; flex-direction: column; align-items: center; justify-content: center; gap: 60px;
  }
  .card {
    position: relative; width: 520px; height: 297px;
    border-radius: 16px; overflow: hidden;
  }

  /* Side one */
  .card--front {
    background: linear-gradient(135deg, var(--navy) 0%, var(--navy-deep) 100%);
  }
  .brand {
    display: flex; align-items: center; gap: 12px;
  }
  .brand__mark { width: 30px; height: 30px; background: var(--teal); }
  .brand__name { font-weight: 700; letter-spacing: 0.5px; }
  .card--front .brand {
    position: absolute; left: 0; right: 0; top: 104px; justify-content: center;
  }
  .card--front .brand__name { color: var(--white); font-size: 42px; }
  .tagline-row {
    position: absolute; left: 30px; right: 30px; top: 182px;
    display: flex; align-items: center; gap: 14px;
  }
  .tagline-row__rule { flex: 1; height: 1px; background: var(--rule-light); }
  .tagline {
    color: var(--white); font-size: 13px; font-weight: 400; letter-spacing: 2.5px; text-transform: uppercase;
  }
  .front-rule {
    position: absolute; left: 0; right: 0; bottom: 44px; height: 1px; background: var(--rule-light); opacity: 0.6;
  }

  /* Side two */
  .card--back { background: var(--white); }
  .card--back svg { position: absolute; inset: 0; }
  .card--back .brand { position: absolute; left: 34px; top: 62px; gap: 10px; }
  .card--back .brand__mark { width: 24px; height: 24px; }
  .card--back .brand__name { color: var(--navy); font-size: 30px; }
  .contact {
    position: absolute; left: 44px; top: 118px; color: var(--teal); font-size: 13px; line-height: 1.45;
  }
  .contact__rule { width: 190px; height: 1px; background: var(--rule-dark); margin: 12px 0; }
  .contact__web strong { color: var(--navy); font-weight: 500; }
  .person {
    position: absolute; right: 30px; bottom: 58px; text-align: right; color: var(--white);
  }
  .person__name { font-size: 24px; font-weight: 500; letter-spacing: 0.5px; }
  .person__role { font-size: 11px; letter-spacing: 1.5px; text-transform: uppercase; margin-top: 2px; }
  .person__rule { width: 180px; height: 1px; background: var(--rule-light); margin: 8px 0 0 auto; }
</style>
</head>
<body>
<main class="sheet">
  <section class="card card--front" aria-label="Card side one">
    <div class="brand">
      <span class="brand__mark"></span>
      <span class="brand__name">Brightway Inc.</span>
    </div>
    <div class="tagline-row">
      <span class="tagline-row__rule"></span>
      <span class="tagline">Where Shine Counts</span>
      <span class="tagline-row__rule"></span>
    </div>
    <div class="front-rule"></div>
  </section>

  <section class="card card--back" aria-label="Card side two">
    <svg width="520" height="297" viewBox="0 0 520 297" aria-hidden="true">
      <defs>
        <linearGradient id="panelNavy" x1="0" y1="0" x2="1" y2="1">
          <stop offset="0" stop-color="#1d2663"/>
          <stop offset="1" stop-color="#151c4d"/>
        </linearGradient>
      </defs>
      <path d="M378 0 C362 150 260 270 20 297 L520 297 L520 0 Z" fill="#5fd3d0"/>
      <path d="M386 0 C372 154 272 274 40 297 L520 297 L520 0 Z" fill="#22b8b8"/>
      <path d="M396 0 C384 158 290 278 64 297 L520 297 L520 0 Z" fill="url(#panelNavy)"/>
    </svg>
    <div class="brand">
      <span class="brand__mark"></span>
      <span class="brand__name">Brightway Inc.</span>
    </div>
    <div class="contact">
      <p>418 Harbour Road Suite 7<br>Oakville ON L6K 2B4</p>
      <div class="contact__rule"></div>
      <p>905-555-0147</p>
      <p>info@brightwayservices.ca</p>
      <p class="contact__web">www.<strong>thebrightway</strong>.ca</p>
    </div>
    <div class="person">
      <p class="person__name">MARA ELLISON</p>
      <p class="person__role">Director</p>
      <div class="person__rule"></div>
    </div>
  </section>
</main>
</body>
</html>
```